Orva Business Card

we need a business card for flooring business called Orva Flooring, the design should be black and white. we have 2 locations

Harrowvale Showroom
527 Kellerman Road,
Harrowvale VIC 3188

Kestonmere Showroom
462 Bramwell Hwy,
Kestonmere VIC 3276

email : sales@orvaflooring.com.au
(03) 9471 2830

Please inform we sell , Laminate, Hybrid, Timber, carpet and commercial flooring

```html
<!DOCTYPE html>
<html lang="en">
<head>
<meta charset="UTF-8">
<title>Orva Flooring Business Card</title>
<link href="https://fonts.googleapis.com/css2?family=Lato:ital,wght@0,300;0,400;0,700;0,900;1,700&display=swap" rel="stylesheet">
<style>
  :root {
    --bg: #2b2b2b;
    --bg-deep: #0f0f0f;
    --card: #231f20;
    --white: #ffffff;
    --soft: #d9d9d9;
    --muted: #7d7d7d;
    --rule: #8a8a8a;
  }
  * { margin: 0; padding: 0; box-sizing: border-box; }
  html, body { width: 1200px; height: 875px; overflow: hidden; }
  body {
    background: radial-gradient(ellipse at 50% 40%, var(--bg) 0%, var(--bg-deep) 100%);
    font-family: "Lato", Arial, sans-serif;
    color: var(--white);
    display: flex;
    align-items: center;
    justify-content: center;
    gap: 40px;
  }
  .card {
    width: 540px;
    height: 310px;
    background: var(--card);
    border-radius: 24px;
    position: relative;
    box-shadow: 0 18px 40px rgba(0,0,0,0.55);
  }
  .wordmark {
    font-family: "Lato", Arial, sans-serif;
    font-weight: 300;
    color: var(--white);
    text-transform: uppercase;
    letter-spacing: 6px;
    line-height: 1.15;
    text-align: center;
  }
  .wordmark .brand { display: block; font-size: 64px; letter-spacing: 10px; }
  .wordmark .trade { display: block; font-size: 30px; }

  .card-front .wordmark {
    position: absolute;
    top: 70px;
    left: 0; right: 0;
  }
  .tagline {
    position: absolute;
    bottom: 34px;
    left: 0; right: 0;
    text-align: center;
    font-size: 14px;
    letter-spacing: 0.4px;
    color: var(--white);
  }
  .tagline strong { font-weight: 700; font-style: italic; }

  .card-back .wordmark {
    position: absolute;
    top: 100px;
    left: 30px;
    width: 230px;
  }
  .card-back .wordmark .brand { font-size: 50px; letter-spacing: 7px; }
  .card-back .wordmark .trade { font-size: 24px; letter-spacing: 5px; }
  .divider {
    position: absolute;
    left: 282px;
    top: 60px;
    width: 1px;
    height: 200px;
    background: var(--rule);
  }
  .details {
    position: absolute;
    left: 304px;
    top: 42px;
    font-size: 13px;
    line-height: 1.35;
  }
  .person-name {
    font-size: 19px;
    font-weight: 900;
    color: var(--muted);
    letter-spacing: 0.5px;
    text-transform: uppercase;
  }
  .person-role { font-size: 14px; margin-bottom: 8px; }
  .showroom { margin-bottom: 8px; }
  .showroom-label { color: var(--muted); }
  .contact-list { list-style: none; margin-top: 4px; }
  .contact-list li { display: flex; align-items: center; gap: 8px; }
  .contact-list svg { width: 11px; height: 11px; flex: none; }
  .icon-fill { fill: var(--soft); }
  .icon-line { fill: none; stroke: var(--soft); stroke-width: 2.5; }
</style>
</head>
<body>

  <section class="card card-front" aria-label="Card front">
    <div class="wordmark">
      <span class="brand">Orva</span>
      <span class="trade">Flooring</span>
    </div>
    <p class="tagline"><strong>We Sell</strong>, Laminate, Hybrid, Timber, Carpet &amp; Commercial Flooring</p>
  </section>

  <section class="card card-back" aria-label="Card back">
    <div class="wordmark">
      <span class="brand">Orva</span>
      <span class="trade">Flooring</span>
    </div>
    <div class="divider"></div>
    <div class="details">
      <p class="person-name">Liam Carter</p>
      <p class="person-role">Founder &amp; CEO</p>
      <div class="showroom">
        <p class="showroom-label">Harrowvale Showroom</p>
        <p>527 Kellerman Road</p>
        <p>Harrowvale VIC 3188</p>
      </div>
      <div class="showroom">
        <p class="showroom-label">Kestonmere Showroom</p>
        <p>462 Bramwell Hwy</p>
        <p>Kestonmere VIC 3276</p>
      </div>
      <ul class="contact-list">
        <li>
          <svg class="icon-fill" viewBox="0 0 24 24" aria-hidden="true"><path d="M6.6 10.8a15.1 15.1 0 0 0 6.6 6.6l2.2-2.2a1 1 0 0 1 1-.25 11.4 11.4 0 0 0 3.6.57 1 1 0 0 1 1 1V20a1 1 0 0 1-1 1A17 17 0 0 1 3 4a1 1 0 0 1 1-1h3.5a1 1 0 0 1 1 1 11.4 11.4 0 0 0 .57 3.6 1 1 0 0 1-.25 1z"/></svg>
          <span>(03) 9471 2830</span>
        </li>
        <li>
          <svg class="icon-line" viewBox="0 0 24 24" aria-hidden="true"><path d="M2 5h20v14H2z M2 5l10 8 10-8"/></svg>
          <span>sales@orvaflooring.com.au</span>
        </li>
        <li>
          <svg class="icon-line" viewBox="0 0 24 24" aria-hidden="true"><circle cx="12" cy="12" r="9.5"/><path d="M2.5 12h19 M12 2.5c3 3 3 16 0 19 M12 2.5c-3 3-3 16 0 19"/></svg>
          <span>orvaflooring.com.au</span>
        </li>
      </ul>
    </div>
  </section>

</body>
</html>
```